Quillfern Litigation Funding Letterhead & Document Template

We need a letter head designed for our fund. Our fund works with law firms and investors across the globe. We need a a cover letter template as well as a document template for subsequent pages. Blue and white color scheme is preferred. This is our predecessor's website: https://www.quillfernlc.com/index.html. Please see our logo attached. The logo color code is #19478d. Font is Gotham-Medium.
Target Market(s)
Sophisticated investors and law firms
Font styles to use
Sans Serif
Colors
0255a3

```html
<!DOCTYPE html>
<html lang="en">
<head>
<meta charset="UTF-8">
<title>Quillfern Litigation Funding – Letterhead</title>
<link href="https://fonts.googleapis.com/css2?family=Montserrat:wght@400;500;600&family=Tinos&display=swap" rel="stylesheet">
<style>
  :root {
    --brand: #19478d;
    --brand-light: #2f7fc1;
    --ink: #1f3f7a;
    --paper: #ffffff;
    --backdrop: #e9eaec;
  }
  * { box-sizing: border-box; margin: 0; padding: 0; }
  html, body { width: 1200px; height: 800px; overflow: hidden; }
  body {
    background: var(--backdrop);
    font-family: "Montserrat", Arial, sans-serif;
    color: var(--ink);
  }
  .letterhead {
    position: absolute;
    left: 330px; top: 20px;
    width: 540px; height: 760px;
    background: var(--paper);
    box-shadow: 0 2px 10px rgba(0,0,0,0.08);
    overflow: hidden;
  }
  .brand {
    position: absolute; left: 44px; top: 48px;
    display: flex; align-items: center; gap: 8px;
  }
  .brand-square { width: 14px; height: 14px; background: var(--brand); }
  .brand-name {
    font-weight: 600; font-size: 12px; letter-spacing: 0.6px;
    color: var(--brand); text-transform: uppercase;
  }
  .contact-box {
    position: absolute; right: 0; top: 92px;
    width: 190px;
    background: var(--brand); color: #fff;
    padding: 11px 14px 11px 14px;
    font-size: 7.5px; line-height: 12px;
  }
  .contact-box li {
    list-style: none; display: flex; justify-content: flex-end;
    align-items: center; gap: 6px; white-space: nowrap;
  }
  .contact-box li.plain { padding-right: 13px; }
  .contact-box svg { width: 7px; height: 7px; fill: #fff; flex: none; }
  .recipient {
    position: absolute; left: 44px; top: 140px; font-size: 8px; line-height: 12px;
  }
  .recipient .date { margin-bottom: 5px; }
  .recipient .name { color: var(--brand-light); font-weight: 500; font-size: 10px; line-height: 14px; }
  .salutation {
    position: absolute; left: 0; right: 0; top: 250px;
    text-align: center; font-weight: 600; font-size: 11px; letter-spacing: 1px;
  }
  .body-copy {
    position: absolute; left: 44px; right: 44px; top: 280px;
    font-size: 8px; line-height: 13px;
  }
  .body-copy p { margin-bottom: 13px; }
  .sign-off {
    position: absolute; right: 60px; top: 610px; width: 110px; text-align: center;
  }
  .signature { width: 40px; height: 30px; margin: 0 auto 6px; background: linear-gradient(#eef1f7,#e3e8f2); }
  .sign-name { font-family: "Tinos", serif; font-size: 11px; }
  .sign-role { font-family: "Tinos", serif; font-size: 8px; color: var(--brand-light); }
  .web-band {
    position: absolute; left: 0; top: 690px;
    width: 210px; height: 22px; background: var(--brand); color: #fff;
    font-size: 8px; font-weight: 500; letter-spacing: 1px;
    display: flex; align-items: center; padding-left: 40px;
  }
  .footer-square {
    position: absolute; right: 40px; bottom: 24px;
    width: 12px; height: 12px; background: var(--brand);
  }
</style>
</head>
<body>
  <main class="letterhead">
    <header class="brand">
      <span class="brand-square"></span>
      <span class="brand-name">Quillfern Litigation Funding</span>
    </header>

    <ul class="contact-box">
      <li>+1 (555) 014-7200 <svg viewBox="0 0 10 10"><path d="M2 0l2 2-1 1.5a6 6 0 0 0 3.5 3.5L8 6l2 2-1.5 2C4 10 0 6 0 1.5z"/></svg></li>
      <li>+1 (555) 014-7300 <svg viewBox="0 0 10 10"><rect x="2" y="0" width="6" height="3"/><rect x="0" y="3" width="10" height="5"/></svg></li>
      <li>info@quillfernlc.com <svg viewBox="0 0 10 10"><rect x="0" y="2" width="10" height="6"/></svg></li>
      <li>Fenwick Plaza – Upper Floor <svg viewBox="0 0 10 10"><path d="M5 0a3.5 3.5 0 0 1 3.5 3.5C8.5 6 5 10 5 10S1.5 6 1.5 3.5A3.5 3.5 0 0 1 5 0z"/></svg></li>
      <li class="plain">410 Harbor Lane</li>
      <li class="plain">Suite 900, Dallas, TX 75201</li>
    </ul>

    <section class="recipient">
      <p class="date">Wednesday, October 28, 2020</p>
      <p class="name">Mara Ellwood</p>
      <p>18 Heron Ridge Court</p>
      <p>41 Linden Avenue</p>
      <p>Maple Falls Ohio 44012</p>
    </section>

    <h1 class="salutation">DEAR MARA</h1>

    <section class="body-copy">
      <p>Lorem ipsum dolor sit amet, cetero accusamus intellegat at his, usu aeterno erroribus sadipscing id, nam virtute equidem reprimique ea. Est cu modo oblique theophrastus, vix ex ferri dicam iisque, idque nostrud eam ut. Tation constituto repriique ut vis. Cu appareat dissentias qui. Vitae causae ceteros mea an, pro mutat admodum ex, ad quo commodo principes. Eam ignota impetus epicuri no, augue offert in vis. Pro nobis veteem eu, ex ius alia utamur explicari.</p>
      <p>Lorem ipsum dolor sit amet, cetero accusamus intellegat at his, usu aeterno erroribus sadipscing id, nam virtute equidem reprimique ea. Est cu modo oblique theophrastus, vix ex ferri dicam iisque, idque nostrud eam ut. Tation constituto repriique ut vis. Cu appareat dissentias qui.</p>
      <p>Tation constituto reprimique ut vis. Cu appareat dissentias qui. Vitae causae ceteros mea an, pro mutat admodum ex, ad quo commodo principes. Eam ignota impetus epicuri no.</p>
    </section>

    <footer>
      <div class="sign-off">
        <div class="signature" role="img" aria-label="Handwritten signature"></div>
        <p class="sign-name">Enter Your Name</p>
        <p class="sign-role">Lawyer</p>
      </div>
      <div class="web-band">WWW.QUILLFERNLC.COM</div>
      <span class="footer-square"></span>
    </footer>
  </main>
</body>
</html>
```